Business Card For Life Coaching Business For Men

Take my existing logo and apply it to a business card. I would like the logo to be prominent with stylistic text below reading Life Coaching For Men. Contact info should show as:
Dale Hartwig
dale@steadforgepath.com

```html
<!DOCTYPE html>
<html lang="en">
<head>
<meta charset="utf-8">
<title>Steadforge Path — Business Card</title>
<link rel="stylesheet" href="https://fonts.googleapis.com/css2?family=Arimo:wght@400;700&display=swap">
<style>
  :root {
    --backdrop: #3d3d3d;
    --navy: #05039a;
    --navy-deep: #030080;
    --teal: #138a8b;
    --paper: #ffffff;
    --ink-grey: #5a5a5a;
    --rule: #c9c9c9;
  }
  * { box-sizing: border-box; margin: 0; padding: 0; }
  html, body {
    width: 1200px; height: 803px; overflow: hidden;
    background: var(--backdrop);
    font-family: "Arimo", Arial, sans-serif;
  }
  .stage { position: relative; width: 1200px; height: 803px; }

  .card {
    position: absolute; top: 250px;
    width: 525px; height: 300px;
    border-radius: 16px; overflow: hidden;
    box-shadow: 0 14px 30px rgba(0,0,0,.35);
  }

  /* Front */
  .card-front { left: 50px; background: var(--paper); }
  .brand {
    position: absolute; left: 30px; top: 80px;
    display: flex; align-items: center; gap: 12px;
    width: 205px;
  }
  .brand-dot { width: 46px; height: 46px; border-radius: 50%; background: var(--navy); flex: none; }
  .brand-name {
    font-weight: 700; font-size: 20px; line-height: 1.05;
    color: var(--navy); text-transform: uppercase; letter-spacing: .3px;
  }
  .brand-tagline {
    position: absolute; left: 30px; top: 140px; width: 205px;
    font-size: 12px; color: var(--teal); letter-spacing: 1px;
  }
  .divider {
    position: absolute; left: 252px; top: 48px;
    width: 1px; height: 130px;
    background: linear-gradient(to bottom, transparent, var(--rule) 20%, var(--rule) 80%, transparent);
  }
  .contact { position: absolute; left: 274px; top: 40px; }
  .contact-name { font-weight: 700; font-size: 22px; color: var(--navy); margin-bottom: 16px; }
  .contact-line { font-size: 12px; color: var(--ink-grey); line-height: 1.4; }
  .contact-row { display: flex; align-items: center; gap: 7px; font-size: 12px; color: var(--ink-grey); line-height: 1.55; }
  .contact-row svg { width: 10px; height: 10px; flex: none; }
  .contact-block { margin-bottom: 6px; }

  .accent-teal {
    position: absolute; right: 0; top: 188px;
    width: 82px; height: 38px; background: var(--teal);
  }
  .mini-mark {
    position: absolute; right: 92px; top: 196px;
    width: 22px; height: 22px; border-radius: 50%; background: var(--navy);
  }
  .web-band {
    position: absolute; left: 0; right: 82px; top: 226px; height: 36px;
    background: var(--navy);
    display: flex; align-items: center; padding-left: 40px;
    color: var(--paper); font-size: 14px; letter-spacing: 3px;
  }

  /* Back */
  .card-back { left: 625px; background: var(--navy); }
  .back-mark {
    position: absolute; left: 50%; top: 46px; transform: translateX(-50%);
    width: 150px; height: 150px; border-radius: 50%;
    background: var(--navy-deep);
    box-shadow: inset 2px 2px 4px rgba(0,0,0,.25), inset -2px -2px 4px rgba(255,255,255,.06);
  }
  .back-web {
    position: absolute; left: 0; right: 0; bottom: 38px;
    text-align: center; color: var(--paper); font-size: 14px; letter-spacing: .5px;
  }
</style>
</head>
<body>
<div class="stage">
  <section class="card card-front">
    <div class="brand">
      <span class="brand-dot"></span>
      <span class="brand-name">Steadforge<br>Path</span>
    </div>
    <p class="brand-tagline">Life Coaching For Men</p>
    <span class="divider"></span>
    <div class="contact">
      <p class="contact-name">Dale Hartwig</p>
      <div class="contact-block">
        <p class="contact-line">412 Cedar Hollow Road</p>
        <p class="contact-line">Larkfield, Canada 20918</p>
      </div>
      <p class="contact-row">
        <svg viewBox="0 0 10 10"><path d="M2 1 L4 3 L3 4.2 Q4.5 6 5.8 7 L7 6 L9 8 L7.6 9.3 Q4 8.5 .7 2.4 Z" fill="var(--navy)"/></svg>
        555-014-2271
      </p>
      <p class="contact-row">
        <svg viewBox="0 0 10 10"><rect x=".5" y="2" width="9" height="6.5" fill="var(--navy)"/><path d="M.5 2 L5 5.6 L9.5 2" stroke="#fff" stroke-width="1" fill="none"/></svg>
        dale@steadforgepath.com
      </p>
    </div>
    <span class="accent-teal"></span>
    <span class="mini-mark"></span>
    <div class="web-band">www.steadforgepath.com</div>
  </section>

  <section class="card card-back">
    <span class="back-mark"></span>
    <p class="back-web">www.steadforgepath.com</p>
  </section>
</div>
</body>
</html>
```